Etiketten für kalt gepresste Bio-Öle
Zielgruppe
Wir sind ein Bio-Betrieb, der sowohl Gemüse anbaut, als auch gesunde Bio-Lebensmittel herstellt. Gründungsjahr: 1999 - Jetzt werden wir eine Ölmühle dazubekommen und auch frische, kalt gepresste Bio-Öle anbieten. Dazu brauchen wir ein hochwertiges Etikettendesign am Beispiel des Leinöls. Die Öle sind im höheren Preissegment (z.B. 500 ml Leinöl für 17,90 €)
Unsere Zielgruppe sind gesundheitsbewusste Menschen mittleren Einkommens. In der Regel kennen sich unsere Kunden in Ernährungsfragen aus und haben einen hohen Qualitätsanspruch.
Aufgabenstellung
Der Kreativität ist freier Raum gegeben. Was wir ausschließen sind anzügliche Begriffe oder Anspielungen. Es handelt sich um ein hochwertiges Produkt, das zwar den Öko-Aspekt beinhaltet, aber trotzdem modern rüberkommen sollte.
Folgende Inhalte muss das Etikett enthalten:
- Firmenlogo (Ölmanufaktur sun4all - ein vorhandenes Logo ist hier nicht vorgegeben)
- Produktname (z.B. Leinöl - aus brauner Leinsaat)
- Bio-Siegel (DE-ÖKO-874 EU-/Nicht-EU-Landwirtschaft)
- Zutatenliste (z.B. 100% kalt gepresstes Bio-Leinöl aus brauner Leinsaat)
- Mindesthaltbarkeitsdatum
- Nährwertangeben (Brennwerte, Kohlenhydrate, Zucker, Fett, gesättigte Fettsäuren, Eiweiß, Salz)
- Barcode
- Füllmenge (z.B. 500 ml)
- Produktbeschreibung (siehe Dateiupload)
- Empfehlung (z.B. Das Leinöl ist ein Qualitätsprodukt. Es sollte frisch innerhalb von 3 Wochen verzehrt werden. Kühl und dunkel lagern.)
Die 500ml Flasche kann unter folgendem Link eingesehen werden:
https://www.flaschora-shop.example/velira-500ml-antikglas-kbt.-pp-482.html
Durchmesser 60,3 mm, Höhe 277,5 mm
Wichtig:
Bitte orientieren Sie sich NICHT an dem Design unserer Webseiten, da wir eine komplett neue Produktlinie aufbauen wollen.

```html
<!DOCTYPE html>
<html lang="de">
<head>
<meta charset="utf-8">
<title>Leinöl – Etiketten</title>
<link href="https://fonts.googleapis.com/css2?family=Outfit:wght@500;600&family=Quicksand:wght@400;600;700&family=Source+Sans+3:wght@400;600&display=swap" rel="stylesheet">
<style>
  :root {
    --backdrop: #bfcdea;
    --label-blue: #7f9bd0;
    --seed-tint: rgba(168, 190, 230, .75);
    --flower-violet: rgba(150, 148, 222, .9);
    --flower-violet-soft: rgba(150, 148, 222, .45);
    --white: #ffffff;
    --ink: #2a2a2a;
    --seal-green: #8bbf3c;
  }
  * { box-sizing: border-box; margin: 0; padding: 0; }
  html, body { width: 999px; height: 1200px; overflow: hidden; }
  body { background: var(--backdrop); position: relative; font-family: "Quicksand", sans-serif; }

  .label { position: absolute; top: 85px; width: 320px; height: 1030px; background: var(--label-blue); color: var(--white); overflow: hidden; }
  .label--front { left: 150px; }
  .label--back { left: 530px; }

  /* front */
  .front__company { position: absolute; top: 40px; left: 0; right: 0; text-align: center; font-weight: 700; font-size: 20px; }
  .seed-field { position: absolute; border-radius: 50%; }
  .seed-field--upper { left: -20px; top: 20px; width: 360px; height: 260px; background: radial-gradient(ellipse at center, var(--seed-tint), transparent 70%); }
  .seed-field--lower { left: 140px; top: 610px; width: 200px; height: 400px; background: radial-gradient(ellipse at center, var(--seed-tint), transparent 70%); }
  .flower-spray { position: absolute; border-radius: 50%; }
  .flower-spray--branch { left: -10px; top: 262px; width: 340px; height: 140px; background: radial-gradient(ellipse at 65% 45%, var(--flower-violet), var(--flower-violet-soft) 45%, transparent 72%); }
  .flower-spray--stem { left: 10px; top: 520px; width: 190px; height: 520px; background: radial-gradient(ellipse at 50% 55%, var(--flower-violet), var(--flower-violet-soft) 50%, transparent 74%); }

  .title-frame { position: absolute; left: 18px; top: 379px; width: 280px; height: 121px; border: 3px solid var(--white); display: flex; align-items: center; justify-content: center; background: var(--label-blue); }
  .title-frame__name { font-family: "Outfit", sans-serif; font-weight: 600; font-size: 86px; line-height: 1; }
  .title-sub { position: absolute; left: 104px; top: 497px; width: 194px; height: 54px; border: 3px solid var(--white); border-top: none; display: flex; align-items: center; justify-content: center; background: var(--label-blue); font-weight: 700; font-size: 17px; }

  /* back */
  .back__copy { position: absolute; left: 30px; right: 28px; top: 56px; font-size: 11.5px; line-height: 22.5px; }
  .back__copy p { margin-bottom: 22.5px; }
  .back__copy strong { font-weight: 700; }
  .back__flowers { position: absolute; left: 141px; top: 620px; width: 190px; height: 80px; border-radius: 50%; background: radial-gradient(ellipse at 60% 50%, var(--flower-violet), var(--flower-violet-soft) 45%, transparent 72%); }
  .back__info { position: absolute; left: 0; right: 0; top: 669px; bottom: 0; background: var(--white); color: var(--ink); font-family: "Source Sans 3", sans-serif; font-size: 11px; line-height: 1.4; }
  .back__best-before { position: absolute; left: 28px; top: 225px; transform: rotate(-90deg); transform-origin: left top; font-size: 11px; line-height: 1.3; white-space: nowrap; }
  .back__best-before span { display: block; }
  .seal { position: absolute; left: 10px; top: 235px; width: 51px; height: 78px; background: var(--seal-green); }
  .seal__code { position: absolute; left: 8px; top: 318px; font-size: 8.5px; font-weight: 600; }
  .back__details { position: absolute; left: 103px; right: 26px; top: 34px; }
  .back__heading { font-weight: 600; }
  .back__ingredients { margin-bottom: 14px; }
  .nutrition { width: 100%; border-collapse: collapse; margin-top: 2px; margin-bottom: 14px; }
  .nutrition td { border-bottom: 1px solid var(--ink); height: 19px; padding: 0; vertical-align: bottom; }
  .nutrition tr:last-child td { border-bottom: none; }
  .nutrition td:last-child { text-align: right; }
  .back__web { margin-top: 6px; font-weight: 600; letter-spacing: .3px; }
</style>
</head>
<body>

<section class="label label--front" aria-label="Vorderseite Etikett">
  <div class="seed-field seed-field--upper" role="img" aria-label="Muster aus verstreuten Leinsamen"></div>
  <div class="seed-field seed-field--lower" role="img" aria-label="Muster aus verstreuten Leinsamen"></div>
  <p class="front__company">sun4all GmbH</p>
  <div class="flower-spray flower-spray--branch" role="img" aria-label="Illustration eines blühenden Leinzweigs mit blauen Blüten"></div>
  <div class="flower-spray flower-spray--stem" role="img" aria-label="Illustration aufrechter Leinstängel mit blauen Blüten und Knospen"></div>
  <div class="title-frame"><h1 class="title-frame__name">Leinöl</h1></div>
  <div class="title-sub">aus reiner Leinsaat</div>
</section>

<section class="label label--back" aria-label="Rückseite Etikett">
  <div class="back__copy">
    <p>Die Leinsaat in <strong>Rohkost-Qualität</strong> liegt bei uns vor – dies ist nicht selbstverständlich. Für das Frisch-Leinöl wird ausschließlich <strong>Bio-Leinsamen</strong> in Rohkostqualität verwendet. Darüberhinaus muss es einen bestimmten Gehalt an Omega-3-Fettsäuren enthalten und einen <strong>feinen</strong>, <strong>reinen</strong> und <strong>nussigen Geschmack</strong> haben.</p>
    <p>Das Frisch-Leinöl wird nach einem eigens entwickelten Verfahren bei <strong>maximal 30° Celsius</strong> gepresst. Dieses Verfahren wurde auf unsere Anregung hin von dem Rohkostliebhabenden Inhaber der Ölmühle entwickelt. Damit Sie auch in den Genuss der wertvollen Lignane kommen, wird dieses Leinöl <strong>nicht gefiltert</strong>. Sie erkennen es an den abgesetzten Trübstoffen.</p>
    <p><strong>Das Leinöl ist ein Qualitätsprodukt.</strong></p>
    <p>Es sollte frisch innerhalb von 3 Wochen verzehrt werden. Kühl und dunkel lagern.</p>
  </div>
  <div class="back__flowers" role="img" aria-label="Kleine Illustration von Leinblüten"></div>

  <div class="back__info">
    <div class="back__best-before"><span>Mindesthaltbarkeitsdatum:</span><span>xx.xx.xxxx</span></div>
    <div class="seal" role="img" aria-label="EU-Bio-Siegel"></div>
    <span class="seal__code">DE-ÖKO-874</span>

    <div class="back__details">
      <p class="back__heading">Zutaten</p>
      <p class="back__ingredients">100% kalt gepresstes Bio-Leinöl<br>aus brauner Leinsaat</p>
      <p class="back__heading">Nährwertangaben (pro 100g)</p>
      <table class="nutrition">
        <tr><td>Brennwert kcal/kJ</td><td>xxx/xxxx</td></tr>
        <tr><td>Kohlenhydrate</td><td>xx g</td></tr>
        <tr><td>Zucker</td><td>xx g</td></tr>
        <tr><td>Fett</td><td>xx g</td></tr>
        <tr><td>gesättigte Fettsäuren</td><td>xx g</td></tr>
        <tr><td>Eiweiß</td><td>xx g</td></tr>
        <tr><td>Salz</td><td>xx g</td></tr>
      </table>
      <p>sun4all GmbH<br>Lindenweg 12, 34567 Musterfeld</p>
      <p class="back__web">www.biokostladen.example</p>
    </div>
  </div>
</section>

</body>
</html>
```